Membership Card for our Survival Company

We need a membership card design, front and back for our VIP Membership program. Membership card must be branded with our logo and convey the idea of survivalism.
All members will receive this physical, plastic card with embossed Full Name and unique Membership ID.
ID formatting: "VIP-XXXXXXX"
See example image here:
https://media.pagebrook.net/7k/48b2c91e0a3d5f7e61b8c4d2a9e03f/VIP-Membership-Card1-Reflect.png
Note, this is just an example. We do not require you to follow the size, format, image, etc. The only things that must be included are the:
1) Logo
2) Full Name
3) Membership ID as per the provided format
Any more questions, please let me know.
Industry/Entity Type
It Company
Contact Information for Business Card
Full Name
VIP-XXXXXXX

```html
<!DOCTYPE html>
<html lang="en">
<head>
<meta charset="utf-8">
<title>WildHold VIP Membership Card</title>
<link href="https://fonts.googleapis.com/css2?family=Montserrat:wght@500;700&display=swap" rel="stylesheet">
<style>
  :root {
    --backdrop: #1c1c1c;
    --card-dark: #2b2b2b;
    --card-dark-edge: #1a1a1a;
    --gold: #d9b24a;
    --gold-soft: #8a6d2a;
    --sky-light: #f0c9ae;
    --sky-mid: #c99a80;
    --ridge: #1e1714;
    --ink: #111111;
    --white: #f2f2f2;
  }
  * { margin: 0; padding: 0; box-sizing: border-box; }
  html, body {
    width: 1200px; height: 873px; overflow: hidden;
    background: var(--backdrop);
    font-family: "Montserrat", Arial, sans-serif;
  }
  .canvas { position: relative; width: 1200px; height: 873px; }

  .card {
    position: absolute;
    width: 520px; height: 328px;
    border-radius: 18px;
    overflow: hidden;
    box-shadow: 0 18px 40px rgba(0,0,0,.55);
  }

  /* Back of card */
  .card-back {
    left: 70px; top: 110px;
    background: linear-gradient(160deg, var(--card-dark) 0%, var(--card-dark-edge) 100%);
  }
  .card-back__ornament {
    position: absolute; left: 90px; top: 48px; width: 340px; height: 232px;
    border-radius: 50%;
    background: radial-gradient(ellipse at center, rgba(217,178,74,.35) 0%, rgba(138,109,42,.18) 45%, rgba(43,43,43,0) 72%);
  }
  .card-back__rule {
    position: absolute; left: 70px; width: 380px; height: 1px; background: var(--gold);
  }
  .card-back__rule--top { top: 136px; }
  .card-back__rule--bottom { top: 192px; }
  .card-back__title {
    position: absolute; left: 0; right: 0; top: 152px;
    text-align: center;
    color: var(--white);
    font-weight: 700; font-size: 20px; letter-spacing: 9px;
    text-shadow: 0 0 6px rgba(255,255,255,.35);
  }

  /* Front of card */
  .card-front {
    left: 610px; top: 420px;
  }
  .card-front__scene {
    position: absolute; inset: 0;
    background:
      linear-gradient(172deg, transparent 62%, var(--ridge) 63%),
      linear-gradient(180deg, var(--sky-mid) 0%, var(--sky-light) 45%, #d9ad92 100%);
  }
  .brand-name {
    position: absolute; left: 200px; top: 38px;
    color: var(--ink); font-weight: 700; font-size: 22px; letter-spacing: 1px;
  }
  .member-name {
    position: absolute; left: 200px; top: 104px;
    color: var(--ink); font-weight: 700; font-size: 20px; letter-spacing: 8px;
  }
  .member-id {
    position: absolute; left: 200px; top: 136px;
    color: var(--gold); font-weight: 700; font-size: 16px; letter-spacing: 1px;
  }
  .card-number {
    position: absolute; left: 36px; bottom: 30px; right: 30px;
    display: flex; justify-content: space-between;
    color: var(--white); font-weight: 500; font-size: 28px; letter-spacing: 4px;
  }
</style>
</head>
<body>
<main class="canvas">

  <section class="card card-back" aria-label="Membership card back">
    <div class="card-back__ornament" role="img" aria-label="Gold scrolling filigree ornament framing the title"></div>
    <div class="card-back__rule card-back__rule--top"></div>
    <div class="card-back__rule card-back__rule--bottom"></div>
    <p class="card-back__title">MEMBERSHIP CARD</p>
  </section>

  <section class="card card-front" aria-label="Membership card front">
    <div class="card-front__scene" role="img" aria-label="Photo of a hiker silhouetted on a rocky ridge against a misty peach sky"></div>
    <p class="brand-name">WildHold</p>
    <p class="member-name">MARCUS HALE</p>
    <p class="member-id">VIP-XXXXXXX</p>
    <p class="card-number"><span>2208</span><span>6905</span><span>7501</span><span>0580</span></p>
  </section>

</main>
</body>
</html>
```